Design Brief for Website Redesign

Client Name: Bluecrest IT
Website: www.bluecrestit.com.au
Industry: Managed IT Services
Target Audience: Small to medium-sized businesses in Australia, requiring IT solutions, IT support, cloud services, and phone systems.

Project Overview
We are seeking a full redesign of the Bluecrest IT website to modernize its look, improve usability, and enhance user experience across devices. The goal is to create a professional, clean, and user-friendly website that reflects our expertise in IT services and appeals to our business clients.

Objectives
Modern Visual Identity: Create a fresh, modern design that aligns with Bluecrest IT's branding.

Improved User Experience: Simplify navigation, improve accessibility, and enhance mobile responsiveness.

Clear Calls to Action: Ensure CTAs are prominent and encourage user engagement.

Enhanced Trust & Credibility: Highlight testimonials, case studies, and industry credentials.

SEO Optimization: Ensure the site is optimized for search engines, including proper heading structures and metadata.
Design Style & Tone
Professional: Clean, modern, and polished to reflect our IT expertise.

Minimalist: Simple layouts, plenty of white space, and easy-to-read typography.

Tech-focused: Subtle tech-themed design elements that reinforce our brand as a leading IT service provider.

Colors: Use our existing brand colors, or propose a color scheme that complements the tech industry while maintaining a professional feel.

Typography: Clear, readable fonts that convey professionalism and trustworthiness.

Key Pages & Features
Home Page:

Hero section with a clear value proposition.

Highlight key services (IT support, cloud solutions, phone systems, etc.) with icons and brief descriptions.

Prominent CTAs (e.g., “Request a Quote,” “Book a Demo”).

Testimonials from satisfied clients.

Services Page:

Detailed breakdown of the services we offer (IT support, cloud services, phone systems, etc.).

Use of icons or illustrations to make the services visually engaging.

Clear CTAs to request quotes or book consultations.

About Us Page:

Information about our company history, mission, and team.

Highlight our certifications, partnerships, and industry expertise.

Case Studies/Testimonials Page:

Showcase client success stories and testimonials with visuals and brief case study summaries.

Include a trust-building section with logos of major clients or partners.

Contact Page:

Simple contact form for inquiries.

Integrated map with office location.

Social media links and phone number.

Blog/Resource Section:

Easy-to-navigate blog section for IT-related articles, tips, and industry news.

Clear categorization and tags for easy browsing.

Knowledge Base/Support Page:

Self-service area for clients to find articles, FAQs, and support guides.

Option to submit a support ticket.

Mobile Responsiveness:

Ensure the design is fully responsive, with no horizontal scrolling or misaligned content on mobile.

Functional Requirements
Fast Load Times: Optimize images, minimize unnecessary scripts, and ensure the site loads quickly on both desktop and mobile.

User-Friendly CMS: We need a CMS that is easy to update (preferably WordPress, but open to other suggestions).

SEO Best Practices: Structure the site with proper metadata, alt tags, and semantic HTML for better search engine optimization.

Security: Ensure the website follows security best practices (SSL, HTTPS).

Deliverables
Full website design (desktop and mobile versions).

Design mockups in Photoshop, Sketch, or Figma (whichever is preferred).

Working prototype (optional).

Final website files, including images and assets.

A style guide for ongoing consistency.

Industry/Entity Type

IT Managed Services

Number of Pages Required

3 page

Requirements
Must have
• EXCELLENT UX/UI

```html
<!DOCTYPE html>
<html lang="en">
<head>
<meta charset="utf-8">
<title>Bluecrest IT – Technology Solutions for a Better Business</title>
<link rel="stylesheet" href="https://fonts.googleapis.com/css2?family=Archivo+Black&family=Montserrat:ital,wght@0,400;0,500;0,600;0,700;1,400&display=swap">
<style>
:root{
  --red:#e30613;
  --ink:#1b1b1b;
  --text:#555;
  --grey:#e9e9e9;
  --panel:#e6e6e6;
  --dark:#2a2a2d;
  --footer:#222224;
  --white:#fff;
}
*{box-sizing:border-box;margin:0;padding:0}
html,body{width:1200px;height:4870px;overflow:hidden}
body{font-family:"Montserrat",sans-serif;color:var(--ink);background:var(--white);position:relative}
.display{font-family:"Archivo Black",sans-serif;font-weight:400}
.abs{position:absolute}
.btn{position:absolute;background:var(--red);color:var(--white);font-size:14px;font-weight:500;display:flex;align-items:center;justify-content:center;height:40px}
.ph{position:absolute}

/* header */
.site-header{position:absolute;top:0;left:0;width:1200px;height:90px;background:var(--white)}
.brand{position:absolute;left:88px;top:22px;font-family:"Montserrat",sans-serif;font-weight:700;font-size:38px;color:var(--red);letter-spacing:-1px}
.main-nav{position:absolute;left:338px;top:37px;width:604px;display:flex;justify-content:space-between;font-size:11.5px;color:#555;white-space:nowrap}
.contact-btn{left:967px;top:22px;width:144px;height:46px;font-size:14px}

/* hero */
.hero{position:absolute;top:90px;left:0;width:1200px;height:638px;background:linear-gradient(120deg,#3d2a24 0%,#5a463e 30%,#2f3a4a 65%,#4a3a3a 100%)}
.hero h1{position:absolute;left:88px;top:158px;font-size:56px;line-height:62px;color:var(--white)}
.hero p{position:absolute;left:88px;top:352px;width:460px;font-size:12.5px;line-height:19px;color:var(--white)}
.hero .btn{left:88px;top:432px;width:172px;height:42px}
.hero-slider{position:absolute;left:455px;top:592px;width:260px;height:2px;background:var(--white)}

/* about */
.about-img{left:151px;top:833px;width:412px;height:441px;background:linear-gradient(135deg,#3b3f46,#7a5c45 55%,#2c2f35)}
.about h2{position:absolute;left:604px;top:868px;font-size:34px;line-height:36px}
.about h3{position:absolute;left:604px;top:992px;font-size:18px;line-height:22px;color:var(--red)}
.about p{position:absolute;left:604px;width:440px;font-size:12.5px;line-height:20px;color:var(--text)}
.about .btn{left:604px;top:1192px;width:128px;height:40px}

/* services */
.services h2{position:absolute;left:0;width:1200px;top:1380px;text-align:center;font-size:34px;line-height:40px}
.services .lead{position:absolute;left:280px;width:640px;top:1474px;text-align:center;font-size:13px;line-height:20px;color:var(--text)}
.tabs{position:absolute;left:166px;top:1544px;width:335px}
.tab{height:64px;margin-bottom:7px;background:var(--grey);border-left:3px solid #ccc;font-family:"Archivo Black",sans-serif;font-size:16px;display:flex;align-items:center;padding-left:22px}
.tab.active{background:var(--red);color:var(--white);border-left-color:var(--red)}
.service-panel{position:absolute;left:622px;top:1544px;width:412px;height:276px;background:var(--panel);text-align:center}
.service-panel h4{font-family:"Archivo Black",sans-serif;font-size:17px;margin-top:128px}
.service-panel p{font-size:12px;line-height:19px;color:var(--text);width:310px;margin:10px auto 0}
.service-icon{position:absolute;left:166px;top:30px}
.services .btn{left:762px;top:1849px;width:128px;height:42px}

/* why */
.why{position:absolute;top:2000px;left:0;width:1200px;height:635px;background:linear-gradient(180deg,#2b2b2f 0%,#343438 50%,#3a322e 100%)}
.why h2{position:absolute;top:68px;left:0;width:1200px;text-align:center;color:var(--white);font-size:34px;line-height:40px}
.why-cards{position:absolute;left:89px;top:175px;width:1022px;height:339px;background:#5a5a5d;padding:8px;display:flex;gap:8px}
.why-card{position:relative;flex:1;height:323px}
.why-card span{position:absolute;left:18px;bottom:20px;color:var(--white);font-family:"Archivo Black",sans-serif;font-size:18px;line-height:21px}
.why .btn{left:516px;top:555px;width:168px;height:42px}

/* testimonials */
.testimonials h2{position:absolute;top:2726px;left:0;width:1200px;text-align:center;font-size:34px}
.quote{position:absolute;left:230px;width:740px;top:2778px;text-align:center;font-style:italic;font-size:16.5px;line-height:26px;color:#444}
.quote-by{position:absolute;top:2892px;left:0;width:1200px;text-align:center;color:var(--red);font-family:"Archivo Black",sans-serif;font-size:13px}
.arrow{position:absolute;width:44px;height:40px;display:flex;align-items:center;justify-content:center}
.arrow.dark{background:var(--ink)}
.arrow.red{background:var(--red)}

/* customers */
.customers h2{position:absolute;top:2988px;left:0;width:1200px;text-align:center;font-size:34px}
.client{position:absolute;top:3062px;width:242px;height:92px;background:var(--white);box-shadow:0 4px 14px rgba(0,0,0,.12);display:flex;align-items:center;justify-content:center;font-weight:700;font-size:18px;color:#444}

/* resources */
.resources h2{position:absolute;top:3306px;left:0;width:1200px;text-align:center;font-size:34px}
.post{position:absolute;top:3372px;width:308px;height:395px;background:#ececec}
.post-img{position:absolute;left:0;top:0;width:308px;height:205px}
.post-date{position:absolute;left:18px;top:196px;background:var(--red);color:var(--white);font-size:12px;padding:4px 26px}
.post h3{position:absolute;left:18px;top:230px;width:272px;font-family:"Archivo Black",sans-serif;font-size:15px;line-height:19px}
.post p{position:absolute;left:18px;top:300px;width:272px;font-size:12px;line-height:19px;color:#777}
.resources .btn{left:535px;top:3823px;width:130px;height:42px}

/* contact */
.contact h2{position:absolute;left:88px;top:4040px;width:560px;font-size:34px;line-height:36px}
.contact p{position:absolute;left:88px;top:4198px;width:520px;font-size:12.5px;line-height:20px;color:var(--text)}
.contact-form{position:absolute;left:705px;top:3946px;width:405px;height:431px;background:var(--red)}
.field{position:absolute;background:var(--white);font-size:12.5px;color:#888;padding:14px 16px}
.submit{position:absolute;left:126px;top:364px;width:142px;height:40px;background:var(--ink);color:var(--white);font-size:14px;display:flex;align-items:center;justify-content:center}

/* footer */
.site-footer{position:absolute;top:4479px;left:0;width:1200px;height:391px;background:var(--footer);color:var(--white)}
.footer-brand{position:absolute;left:114px;top:92px;font-weight:700;font-size:62px;color:var(--red);letter-spacing:-2px}
.social{position:absolute;left:172px;top:185px;display:flex;gap:20px}
.social span{width:40px;height:40px;border-radius:50%;display:block}
.footer-col{position:absolute;top:66px;border-left:2px solid var(--red);padding-left:10px}
.footer-col h5{font-size:18px;font-weight:500;margin-bottom:18px}
.footer-col li{list-style:none;font-size:12px;line-height:22.5px;color:#ddd}
.footer-bottom{position:absolute;left:88px;top:331px;width:1023px;border-top:1px solid #444;padding-top:22px;font-size:12px;display:flex;justify-content:space-between}
</style>
</head>
<body>

<header class="site-header">
  <div class="brand">Bluecrest</div>
  <nav class="main-nav">
    <span>Our Services ⌄</span><span>Team Chat</span><span>Partners</span><span>Remote</span><span>Resources</span><span>About Us</span><span>Shop</span>
  </nav>
  <a class="btn contact-btn">Contact Us</a>
</header>

<section class="hero" role="img" aria-label="Night city skyline with glowing network lines and a location pin">
  <h1 class="display">Technology<br>Solutions for a<br>better business</h1>
  <p>We understand that technology is a critical component of running a successful business, and that's why we're here to help you navigate the ever-changing landscape of IT...</p>
  <a class="btn">View All Service</a>
  <div class="hero-slider"></div>
  <svg class="abs" style="left:449px;top:584px" width="272" height="18" viewBox="0 0 272 18"><path d="M10 1 L1 9 L10 17" fill="none" stroke="#fff" stroke-width="2"/><path d="M262 1 L271 9 L262 17" fill="none" stroke="#fff" stroke-width="2"/></svg>
</section>

<section class="about">
  <div class="ph about-img" role="img" aria-label="Technician working on cables in a server rack"></div>
  <h2 class="display">Innovative Technology<br>Solutions for Better<br>Business...</h2>
  <h3 class="display">Your Trusted IT Company for Managed<br>IT Services Sydney</h3>
  <p style="top:1054px">We're Bluecrest IT, a Managed IT Services in Sydney provider. We offer expert IT Solutions and Support for Small and Medium Businesses.</p>
  <p style="top:1110px">We are committed to listening to you, understanding your business needs, and providing IT Strategy and Support that aligns with your company's culture and bottom line.</p>
  <a class="btn">Learn More</a>
</section>

<section class="services">
  <h2 class="display">Providing Cutting-Edge IT Solutions to<br>Mid-Market Sydney Businesses</h2>
  <p class="lead">We can provide for all of your IT needs and keep your systems running smoothly, securely, and efficiently. Our services include:</p>
  <div class="tabs">
    <div class="tab active">Proactive Monitoring</div>
    <div class="tab">Help Desk Support</div>
    <div class="tab">Disaster Recovery</div>
    <div class="tab">IT Project Management</div>
    <div class="tab">Internet Connections</div>
  </div>
  <div class="service-panel">
    <svg class="service-icon" width="82" height="82" viewBox="0 0 82 82" fill="none" stroke="#1b1b1b" stroke-width="2">
      <rect x="4" y="16" width="74" height="56"/>
      <line x1="4" y1="26" x2="78" y2="26"/>
      <rect x="16" y="52" width="8" height="16"/><rect x="30" y="44" width="8" height="24"/><rect x="44" y="48" width="8" height="20"/><rect x="58" y="36" width="8" height="32"/>
      <polyline points="14,44 32,34 46,40 66,26"/>
      <circle cx="16" cy="10" r="7"/>
    </svg>
    <h4>Proactive Monitoring</h4>
    <p>24 hr monitoring of your network and systems to detect and resolve issues before they become problems.</p>
  </div>
  <a class="btn">View More</a>
</section>

<section class="why" role="img" aria-label="Darkened city skyline backdrop">
  <h2 class="display">Why Bluecrest IT? We Think Ahead,<br>with You in Mind.</h2>
  <div class="why-cards">
    <div class="why-card" role="img" aria-label="Two colleagues reviewing a laptop in a server room" style="background:linear-gradient(180deg,#6d7d8a,#3b4350)"><span>Reliable IT<br>Support</span></div>
    <div class="why-card" role="img" aria-label="Engineer checking a laptop beside network equipment" style="background:linear-gradient(180deg,#5e6670,#2f343b)"><span>Robust Cyber<br>Security</span></div>
    <div class="why-card" role="img" aria-label="Technician with a laptop in a data centre aisle" style="background:linear-gradient(180deg,#8a9098,#3a3e45)"><span>CloudOffice 365<br>Support</span></div>
    <div class="why-card" role="img" aria-label="Professional standing in a blue-lit data centre" style="background:linear-gradient(180deg,#2f5a7a,#1f2c3a)"><span>Cloud Backup<br>Solutions</span></div>
  </div>
  <a class="btn">View All Service</a>
</section>

<section class="testimonials">
  <h2 class="display">What Our Clients Say</h2>
  <a class="arrow dark" style="left:89px;top:2804px"><svg width="18" height="14" viewBox="0 0 18 14" fill="none" stroke="#fff" stroke-width="1.6"><path d="M17 7H2M7 1L1 7l6 6"/></svg></a>
  <p class="quote">The guys at Bluecrest IT were fantastic to deal with when helping us build our website from scratch. They helped us with everything from the marketing strategy, the colour scheme, the design &amp; the logo. We are very impressed with the outcome and highly recommend them.</p>
  <div class="quote-by">Tallow Tool Depot</div>
  <a class="arrow red" style="left:1067px;top:2804px"><svg width="18" height="14" viewBox="0 0 18 14" fill="none" stroke="#fff" stroke-width="1.6"><path d="M1 7h15M11 1l6 6-6 6"/></svg></a>
</section>

<section class="customers">
  <h2 class="display">Some customers we support</h2>
  <div class="client" style="left:89px">Harbourline Realty</div>
  <div class="client" style="left:349px">Kestrel &amp; Co</div>
  <div class="client" style="left:609px">Meridian Homes</div>
  <div class="client" style="left:868px">Northgate Property</div>
  <a class="arrow dark" style="left:549px;top:3189px"><svg width="18" height="14" viewBox="0 0 18 14" fill="none" stroke="#fff" stroke-width="1.6"><path d="M17 7H2M7 1L1 7l6 6"/></svg></a>
  <a class="arrow red" style="left:606px;top:3189px"><svg width="18" height="14" viewBox="0 0 18 14" fill="none" stroke="#fff" stroke-width="1.6"><path d="M1 7h15M11 1l6 6-6 6"/></svg></a>
</section>

<section class="resources">
  <h2 class="display">Helpful Resourses</h2>
  <article class="post" style="left:119px">
    <div class="post-img" role="img" aria-label="Hands typing on a keyboard" style="background:linear-gradient(180deg,#555,#1e1e1e)"></div>
    <span class="post-date">April 11, 2025</span>
    <h3>Mailbox Rules: What They Are and How to Use Them Effectively</h3>
    <p>Automate Your Inbox and Boost Productivity Managing your inbox can feel like a full-time job, especially when emails keep pouring in...</p>
  </article>
  <article class="post" style="left:446px">
    <div class="post-img" role="img" aria-label="City at dusk overlaid with connected network icons" style="background:linear-gradient(180deg,#3f6e9a,#1e3550)"></div>
    <span class="post-date">April 9, 2025</span>
    <h3>The Importance of High Speed, Stable Internet for SMBs</h3>
    <p>Poor Connectivity Can Really Hurt Your Business's Digital Lifeline How much does your business depend on the internet? More than you might think...</p>
  </article>
  <article class="post" style="left:771px">
    <div class="post-img" role="img" aria-label="Hands on a laptop with floating email symbols" style="background:linear-gradient(180deg,#cfd8e2,#8fa3b8)"></div>
    <span class="post-date">April 2, 2025</span>
    <h3>Mailbox Blues? How to Fix Common Email Sending &amp; Receiving Issues</h3>
    <p>How to Fix Sending and Receiving Issues Ever hit "send" only to wonder if your email vanished into the digital void? Or waited anxiously for an important...</p>
  </article>
  <a class="btn">View More</a>
</section>

<section class="contact">
  <h2 class="display">Looking for IT Support<br>in Sydney? Explore Managed<br>IT Support Services for<br>Your Business</h2>
  <p>Get help managing IT for your small or medium business from our team based right here in Sydney. Whether your team is working on-site or remotely, Bluecrest IT can help you streamline your operations. Contact us today to schedule a consultation and learn how we can support your business goals.</p>
  <form class="contact-form">
    <div class="field" style="left:17px;top:46px;width:178px;height:48px">Name*</div>
    <div class="field" style="left:207px;top:46px;width:180px;height:48px">Email*</div>
    <div class="field" style="left:17px;top:110px;width:178px;height:48px">Phone*</div>
    <div class="field" style="left:207px;top:110px;width:180px;height:48px">Address*</div>
    <div class="field" style="left:17px;top:168px;width:370px;height:168px">Send A Message*</div>
    <div class="submit">Submit Now</div>
  </form>
</section>

<footer class="site-footer">
  <div class="footer-brand">Bluecrest</div>
  <div class="social" aria-label="Social media links">
    <span style="background:var(--red)"></span><span style="background:#444"></span><span style="background:#444"></span>
  </div>
  <div class="footer-col" style="left:460px"><h5>About us</h5><ul><li>Our Company</li><li>Our Team</li><li>Bluecrest IT Partners</li><li>Contact Us</li></ul></div>
  <div class="footer-col" style="left:676px"><h5>Useful links</h5><ul><li>Services</li><li>Blog</li><li>Videos</li><li>Team Chat</li></ul></div>
  <div class="footer-col" style="left:892px"><h5>Our Solutions</h5><ul><li>IT Support</li><li>Project Management</li><li>IT Consulting and Training</li><li>Hardware and Software</li><li>IT Cyber Security</li><li>Cloud Solutions</li><li>IT Procurement and Auditing</li><li>Mobile and Web Development</li></ul></div>
  <div class="footer-bottom"><span>Copyright Bluecrest IT 2025</span><span>Privacy Policy | Terms &amp; Conditions</span></div>
</footer>

</body>
</html>
```